Accounting business needs business card

I have a business card but need something better. I want the colour changed and the design to be better. I have uploaded a picture of my new sign that is grey in colour, i would like to incorporate these colours.

```html
<!DOCTYPE html>
<html lang="en">
<head>
<meta charset="utf-8">
<title>Kestrel Tax – Business Card</title>
<link rel="stylesheet" href="https://fonts.googleapis.com/css2?family=Montserrat:wght@300;400;700&family=Poppins:wght@300;400&display=swap">
<style>
  :root {
    --bg: #5a5c60;
    --card-blue: #4a6fb8;
    --card-dark: #2b2d31;
    --accent-blue: #4a6fc0;
    --white: #ffffff;
    --badge-blue: #1f5aa6;
    --badge-yellow: #f2c400;
    --partner-blue: #1fb2e8;
    --text-dark: #2b2d31;
  }
  * { margin: 0; padding: 0; box-sizing: border-box; }
  html, body { width: 1200px; height: 965px; overflow: hidden; background: var(--bg); }
  .stage { position: relative; width: 1200px; height: 965px; }

  .card {
    position: absolute;
    width: 640px; height: 366px;
    overflow: hidden;
    box-shadow: 0 12px 30px rgba(0,0,0,.35);
  }

  .brand {
    display: flex; align-items: center; gap: 16px;
    font-family: "Montserrat", sans-serif; font-weight: 400;
    color: var(--white); letter-spacing: 0.38em; text-transform: uppercase;
    white-space: nowrap;
  }
  .brand-mark { border: 2px solid var(--white); border-radius: 50%; flex: none; }

  /* Front */
  .card-front { left: 80px; top: 80px; background: var(--card-blue); }
  .card-front .brand {
    position: absolute; left: 50%; top: 50%; transform: translate(-50%, -50%);
    flex-direction: column; font-size: 34px;
  }
  .card-front .brand-name { margin-right: -0.38em; }
  .card-front .brand-mark { width: 92px; height: 92px; }

  /* Back */
  .card-back { left: 480px; top: 510px; background: var(--card-dark); }
  .card-back .brand {
    position: absolute; right: 38px; top: 40px;
    flex-direction: column; align-items: center; font-size: 28px; gap: 14px;
  }
  .card-back .brand-mark { width: 78px; height: 78px; }

  .card-shapes { position: absolute; inset: 0; }

  .contact-block {
    position: absolute; left: 36px; top: 104px;
    font-family: "Poppins", sans-serif; color: var(--white);
  }
  .contact-block::before {
    content: ""; position: absolute; left: -36px; top: 8px;
    width: 3px; height: 80px; background: var(--white);
  }
  .person-name {
    font-family: "Montserrat", sans-serif; font-weight: 700;
    font-size: 27px; color: var(--accent-blue); line-height: 1.05;
  }
  .person-credentials, .person-role { font-size: 14px; font-weight: 300; line-height: 1.35; }
  .contact-list { list-style: none; margin-top: 12px; }
  .contact-list li {
    display: flex; align-items: center; gap: 12px;
    font-size: 15px; font-weight: 300; line-height: 1.45;
  }
  .contact-list svg { width: 15px; height: 15px; flex: none; }

  .partner-strip {
    position: absolute; left: 24px; bottom: 14px;
    display: flex; align-items: center; gap: 14px;
  }
  .partner-badge { display: flex; width: 140px; height: 40px; }
  .partner-badge .badge-left { flex: 1; background: var(--badge-blue); }
  .partner-badge .badge-right { width: 50px; background: var(--badge-yellow); }
  .partner-note {
    font-family: "Poppins", sans-serif; font-weight: 300;
    font-size: 13px; line-height: 1.15; color: var(--text-dark);
  }
  .partner-circle {
    width: 46px; height: 46px; border-radius: 50%;
    background: var(--partner-blue); margin-bottom: 10px;
  }
</style>
</head>
<body>
<main class="stage">

  <section class="card card-front" aria-label="Card front">
    <div class="brand">
      <span class="brand-mark"></span>
      <span class="brand-name">Kestrel Tax</span>
    </div>
  </section>

  <section class="card card-back" aria-label="Card back">
    <svg class="card-shapes" viewBox="0 0 640 366" preserveAspectRatio="none">
      <polygon points="455,342 640,296 640,316 470,366 462,366" fill="var(--accent-blue)"/>
      <path d="M0,298 L360,262 C388,259 404,266 418,280 L470,366 L0,366 Z" fill="var(--white)"/>
    </svg>

    <div class="brand">
      <span class="brand-mark"></span>
      <span class="brand-name">Kestrel Tax</span>
    </div>

    <div class="contact-block">
      <h1 class="person-name">Owen Halloway</h1>
      <p class="person-credentials">CPA, MTAX, BCOM (Acc &amp; Fin)</p>
      <p class="person-role">Taxation and Business Accountant</p>
      <ul class="contact-list">
        <li>
          <svg viewBox="0 0 24 24" fill="none" stroke="var(--accent-blue)" stroke-width="2"><path d="M5 3h4l2 5-3 2a12 12 0 0 0 6 6l2-3 5 2v4a2 2 0 0 1-2 2A17 17 0 0 1 3 5a2 2 0 0 1 2-2z"/></svg>
          0412 585 306
        </li>
        <li>
          <svg viewBox="0 0 24 24" fill="none" stroke="var(--accent-blue)" stroke-width="2"><rect x="3" y="5" width="18" height="14"/><path d="M3 5l9 8 9-8"/></svg>
          owen@kestreltax.com.au
        </li>
        <li>
          <svg viewBox="0 0 24 24" fill="none" stroke="var(--accent-blue)" stroke-width="2"><circle cx="12" cy="12" r="9"/><path d="M3 12h18M12 3c3 3 3 15 0 18M12 3c-3 3-3 15 0 18"/></svg>
          www.kestreltax.com.au
        </li>
      </ul>
    </div>

    <div class="partner-strip">
      <div class="partner-badge" role="img" aria-label="Professional body membership badge">
        <span class="badge-left"></span><span class="badge-right"></span>
      </div>
      <p class="partner-note">Kestrel Tax is a<br>Member Practice</p>
      <span class="partner-circle" role="img" aria-label="Accounting software partner badge"></span>
    </div>
  </section>

</main>
</body>
</html>
```